Business card required for IT Consultancy Business - Tealbrook Consulting.
Company provides the whole nine yards of services across IT Architecture, design and execution.
Basically we provide consulting services to help businesses make sure their technology is enabling their business strategy.
Design for front and back required.
We would like the front of the card to inlcude:
Name
Title
Mobile number
email address
www.tbkc.com.au
Company logos attached.
Thank you
Industry/Entity Type
Business
Contact Information for Business Card
Name
Title
Mobile number
email address
www.tbkc.com.au
Look and feel
Each slider illustrates characteristics of the customer's brand and the style your logo design should communicate.

```html
<!DOCTYPE html>
<html lang="en">
<head>
<meta charset="utf-8">
<title>Tealbrook Consulting – Business Card</title>
<link href="https://fonts.googleapis.com/css2?family=Open+Sans:wght@400;600;700&display=swap" rel="stylesheet">
<style>
  :root {
    --backdrop: #000000;
    --card: #ffffff;
    --orange: #f05a28;
    --blue: #1b75bc;
    --rule: #d9d9d9;
  }
  * { margin: 0; padding: 0; box-sizing: border-box; }
  html, body {
    width: 1200px; height: 899px; overflow: hidden;
    background: var(--backdrop);
    font-family: "Open Sans", Arial, sans-serif;
  }
  .canvas { position: relative; width: 1200px; height: 899px; }
  .card {
    position: absolute; top: 306px;
    width: 440px; height: 270px;
    background: var(--card);
    border-radius: 9px;
  }
  .card--front { left: 149px; }
  .card--back { left: 608px; }

  .front-mark {
    position: absolute; left: 40px; top: 78px; width: 130px;
    display: flex; flex-direction: column; align-items: center; gap: 10px;
  }
  .mark-dot { width: 54px; height: 54px; border-radius: 50%; background: var(--orange); }
  .mark-name { color: var(--blue); font-weight: 700; font-size: 20px; line-height: 1; }

  .divider {
    position: absolute; left: 213px; top: 72px;
    width: 1px; height: 135px; background: var(--rule);
  }
  .contact { position: absolute; left: 240px; top: 76px; }
  .person-name { font-size: 15.5px; font-weight: 600; line-height: 1.2; }
  .person-name .first { color: var(--orange); }
  .person-name .last { color: var(--blue); }
  .person-title { font-size: 12px; color: var(--blue); margin-top: 1px; }
  .details { list-style: none; margin-top: 25px; }
  .details li {
    display: flex; align-items: center; gap: 7px;
    font-size: 12px; color: var(--blue); line-height: 18px;
  }
  .details svg { width: 9px; height: 9px; flex: none; fill: var(--orange); }

  .back-mark {
    position: absolute; inset: 0;
    display: flex; align-items: center; justify-content: center; gap: 12px;
  }
  .back-mark .mark-dot { width: 40px; height: 40px; }
  .back-mark .mark-name { font-size: 27px; }
</style>
</head>
<body>
<div class="canvas">
  <section class="card card--front">
    <div class="front-mark">
      <span class="mark-dot"></span>
      <span class="mark-name">Tealbrook</span>
    </div>
    <div class="divider"></div>
    <div class="contact">
      <p class="person-name"><span class="first">Marcus</span> <span class="last">Hale</span></p>
      <p class="person-title">Managing Director</p>
      <ul class="details">
        <li>
          <svg viewBox="0 0 10 10" aria-hidden="true"><path d="M2 0.5 L3.6 2.8 L2.8 3.8 Q3.8 5.9 6.2 7.2 L7.2 6.4 L9.5 8 L8.4 9.5 Q4.5 9.3 1.3 5.5 Q0.3 3.2 0.6 1.6 Z"/></svg>
          (044)-555-0192
        </li>
        <li>
          <svg viewBox="0 0 10 10" aria-hidden="true"><path d="M0.5 2 H9.5 V8.5 H0.5 Z M1 2.4 L5 5.6 L9 2.4" /><path d="M1.2 2.6 L5 5.2 L8.8 2.6" fill="none" stroke="#fff" stroke-width="0.8"/></svg>
          hello@tbkc.com.au
        </li>
        <li>
          <svg viewBox="0 0 10 10" aria-hidden="true"><circle cx="5" cy="5" r="4.5"/><path d="M2 4 Q3.5 3 4.5 4.5 Q5.5 6 4 7.5 M6 2 Q7 3.5 8.5 3.5" fill="none" stroke="#fff" stroke-width="0.8"/></svg>
          www.tbkc.com.au
        </li>
      </ul>
    </div>
  </section>

  <section class="card card--back">
    <div class="back-mark">
      <span class="mark-dot"></span>
      <span class="mark-name">Tealbrook Consulting</span>
    </div>
  </section>
</div>
</body>
</html>
```